Law Firm Marketing Post Card to Real Estate Agents

We need a postcard that will be used to market to real estate agents. Something clean, professional and appealing. We're marketing for a specific field (taxes) and are planning on passing out the cards to individual agents and we do not plan on mailing them. We'd like something on the front cover that truly catches someones attention and makes them want to read the back side. Text will read:

Front and Back; front will have very little text. Only the following:
Tax & Legal Strategies for Real Estate Agents
Presented by Birchwell Legal Partners, LLC
5 Tax Strategies Every Real Estate Agent Should Know

BACK COVER:
Most real estate agents are considered 1099 independent contractors, and have never been told that there are money saving strategies that could make a huge difference for them come tax time with just a few easy steps.

With our free consultation, Birchwell has one mission – to teach real estate agents 5 legal and tax planning strategies that could literally save them thousands of dollars.

Please contact us to schedule a one-on-one consultation, or an office presentation, and learn about some of the tax and legal strategies that have helped countless real estate agents and independent contractors:

- Minimize self employment tax
- Deduct 100% of out of pocket medical expenses
- Create wealth
- Deduct 100% of health insurance premiums
- Invest in real estate
- Deduct a portion of a child’s tuition and expenses
- Reduce overall tax liability

For more information, please email our office at: Info@BirchwellLegal.Example.

Target Market(s)

Real Estate Agents

Industry/Entity Type

Real Estate

Requirements
Must have
• Text listed on the front of the card as shown on the attachment.
• Clean, appealing, professional cover.
• must be similar to colors used on our website so that the reader feels like it is from the same company; please include website address on card as well - www.birchwelllegal.example

```html
<!DOCTYPE html>
<html lang="en">
<head>
<meta charset="utf-8">
<title>Birchwell Legal Partners – Real Estate Agent Postcard</title>
<link href="https://fonts.googleapis.com/css2?family=Oswald:wght@500;600&family=Arimo:ital,wght@0,400;0,700;1,700&display=swap" rel="stylesheet">
<style>
  :root {
    --navy: #173a63;
    --white: #ffffff;
    --page: #ffffff;
    --card-edge: #d9dde3;
  }
  * { box-sizing: border-box; margin: 0; padding: 0; }
  html, body {
    width: 815px; height: 1200px; overflow: hidden;
    background: var(--page);
  }
  .card {
    position: absolute; left: 32px; width: 722px;
    background: var(--white); overflow: hidden;
    outline: 1px solid var(--card-edge);
  }
  .card svg.shapes { position: absolute; inset: 0; width: 100%; height: 100%; }

  /* Front */
  .front { top: 32px; height: 570px; }
  .front-title {
    position: absolute; top: 26px; left: 0; width: 100%;
    text-align: center; color: var(--white);
    font-family: "Oswald", sans-serif; font-weight: 600;
    font-size: 27px; letter-spacing: 0.3px;
  }
  .front-tagline {
    position: absolute; left: 54px; top: 466px; color: var(--white);
    font-family: "Oswald", sans-serif; font-weight: 600; line-height: 1.25;
  }
  .front-tagline .headline { font-size: 24px; }
  .front-tagline .presenter { font-size: 20px; }
  .brand {
    display: flex; align-items: center; gap: 8px;
    font-family: "Arimo", sans-serif; font-weight: 700; color: var(--white);
    letter-spacing: 1px;
  }
  .brand .mark { width: 22px; height: 22px; background: var(--white); }
  .front .brand { position: absolute; right: 58px; top: 486px; font-size: 17px; }

  /* Back */
  .back { top: 622px; height: 565px; }
  .back-copy {
    position: absolute; left: 22px; top: 38px; width: 345px;
    font-family: "Arimo", sans-serif; font-size: 12.7px; line-height: 1.5;
    color: var(--white);
  }
  .back-copy p { margin-bottom: 12px; }
  .benefits { margin: 18px 0 0 40px; list-style: disc; }
  .benefits li { padding-left: 4px; line-height: 1.48; }
  .back-footer {
    position: absolute; left: 28px; top: 450px;
    display: flex; align-items: center; gap: 22px; color: var(--white);
  }
  .back .brand { font-size: 14px; }
  .back .brand .mark { width: 16px; height: 16px; }
  .contact { font-family: "Arimo", sans-serif; font-size: 12.7px; line-height: 1.4; }
  .contact .lead { font-weight: 700; font-style: italic; }
</style>
</head>
<body>

<section class="card front">
  <svg class="shapes" viewBox="0 0 722 570" preserveAspectRatio="none">
    <defs>
      <linearGradient id="photoTone" x1="0" y1="0" x2="1" y2="0">
        <stop offset="0" stop-color="#b9ae98"/>
        <stop offset="0.45" stop-color="#6b6e78"/>
        <stop offset="0.7" stop-color="#ece9e3"/>
        <stop offset="1" stop-color="#8a3a2e"/>
      </linearGradient>
    </defs>
    <rect width="722" height="570" fill="var(--navy)"/>
    <path role="img" aria-label="Photo of three smiling real estate professionals in business suits beside tax forms and a wooden gavel"
          d="M0 78 C 240 98, 480 82, 722 56 L722 345 C 500 388, 260 400, 0 368 Z" fill="url(#photoTone)"/>
    <path d="M0 368 C 260 400, 500 388, 722 345 L722 378 C 500 440, 250 452, 0 393 Z" fill="var(--white)"/>
  </svg>

  <h1 class="front-title">5 Tax Strategies Every Real Estate Agent Should Know</h1>

  <div class="front-tagline">
    <p class="headline">Tax &amp; Legal Strategies for Real Estate Agents</p>
    <p class="presenter">Presented by Birchwell Legal Partners, LLC</p>
  </div>

  <div class="brand"><span class="mark"></span>BIRCHWELL</div>
</section>

<section class="card back">
  <svg class="shapes" viewBox="0 0 722 565" preserveAspectRatio="none" aria-hidden="true">
    <path d="M0 0 L368 0 C 398 160, 385 390, 336 565 L0 565 Z" fill="var(--navy)"/>
  </svg>

  <div class="back-copy">
    <p>Most real estate agents are considered 1099 independent contractors, and have never been told that there are money saving strategies that could make a huge difference for them come tax time with just a few easy steps.</p>
    <p>With our free consultation, Birchwell has one mission – to teach real estate agents 5 legal and tax planning strategies that could literally save them thousands of dollars.</p>
    <p>Please contact us to schedule a one-on-one consultation, or an office presentation, and learn about some of the tax and legal strategies that have helped countless real estate agents and independent contractors:</p>
    <ul class="benefits">
      <li>Minimize self employment tax</li>
      <li>Deduct 100% of out of pocket medical expenses</li>
      <li>Create wealth</li>
      <li>Deduct 100% of health insurance premiums</li>
      <li>Invest in real estate</li>
      <li>Deduct a portion of a child’s tuition &amp; expenses</li>
      <li>Reduce overall tax liability</li>
    </ul>
  </div>

  <div class="back-footer">
    <div class="brand"><span class="mark"></span>BIRCHWELL</div>
    <div class="contact">
      <p class="lead">For more information,<br>please email our office at:</p>
      <p>Info@BirchwellLegal.Example</p>
      <p>www.birchwelllegal.example</p>
    </div>
  </div>
</section>

</body>
</html>
```